Health Coaching Brochure for Healthcare Practioners

I am looking to have a tri-fold brochure created marketed towards healthcare practitioners (doctors, nurses, surgeons, etc), to get them to purchase 1-on-1 health coaching from me.
I've provided the text/content (in pdf & pages), my logo, a picture of me, and two color palettes, but please also include lots of white space. I would like to design to be very clean, modern & crisp. Also include additional photos, of doctors, etc taking care of themselves & feeling happy (maybe eating healthy, maybe exercising, feeling good & happy!)
Please also see http://brightoakwellness.com and http://instagram.com/brightoakwellness for a feel of my brand.
Thank you!
Target Market(s)
Healthcare Practioners (mainly based in Los Angeles, for now)
Industry/Entity Type
Healthcare
Look and feel

```html
<!DOCTYPE html>
<html lang="en">
<head>
<meta charset="utf-8">
<title>Bright Oak Wellness – Tri-fold Brochure</title>
<link href="https://fonts.googleapis.com/css2?family=Source+Sans+3:ital,wght@0,400;0,600;0,700;1,400;1,600&family=Open+Sans:wght@400;600&display=swap" rel="stylesheet">
<style>
  :root{
    --page:#ececec;
    --blue:#3b88d6;
    --blue-deep:#2a6fbf;
    --cyan:#1ec6f3;
    --cyan-light:#62dcfb;
    --navy:#1b3a63;
    --ink:#1d2f45;
    --white:#ffffff;
    --photo:#dfe3e8;
  }
  *{margin:0;padding:0;box-sizing:border-box}
  html,body{width:1200px;height:1200px;overflow:hidden;background:var(--page)}
  body{font-family:"Source Sans 3",sans-serif;position:relative}
  .brochure{position:absolute;left:50px;top:199px;width:1100px;height:802px;box-shadow:0 4px 18px rgba(0,0,0,.12)}
  .brochure__art{position:absolute;inset:0}
  .panel{position:absolute;top:0;height:802px}
  .panel--intro{left:0;width:380px}
  .panel--coach{left:380px;width:340px}
  .panel--cover{left:720px;width:380px}
  .photo{position:absolute;border-radius:50%;border:6px solid var(--white)}
  .photo--coach{left:85px;top:52px;width:170px;height:170px;background:radial-gradient(circle at 50% 40%,#b7a59a,#3b2d2a);box-shadow:0 0 0 5px var(--blue-deep)}
  .photo--doctor{left:150px;top:342px;width:200px;height:200px;background:radial-gradient(circle at 50% 45%,#f4f6f9,#cfd6de);box-shadow:0 0 0 8px var(--cyan)}
  .intro__kicker{position:absolute;left:50px;top:62px;color:var(--cyan);font-weight:700;font-size:23px;line-height:1}
  .intro__title{position:absolute;left:50px;top:86px;color:var(--white);font-weight:700;font-size:23px;line-height:1}
  .intro__lead{position:absolute;left:50px;top:117px;width:300px;color:var(--white);font-size:14.5px;line-height:1.15}
  .intro__list{position:absolute;left:50px;top:161px;width:310px;color:var(--white);font-size:12.3px;line-height:1.3;list-style:none}
  .intro__list li{position:relative;padding-left:10px;margin-bottom:1px}
  .intro__list li::before{content:"";position:absolute;left:0;top:6px;width:4px;height:4px;background:var(--white);border-radius:50%}
  .intro__note{position:absolute;left:54px;top:570px;width:305px;color:var(--navy);font-style:italic;font-weight:600;font-size:10.6px;line-height:1.25}
  .intro__call{position:absolute;left:54px;top:624px;color:var(--blue-deep);font-weight:600;font-size:15px}
  .intro__contact{position:absolute;left:54px;top:657px;width:300px;color:var(--navy);font-size:10.6px;line-height:1.45}
  .intro__contact strong{font-weight:700}
  .coach__name{position:absolute;left:0;width:340px;top:232px;text-align:center;color:var(--white);font-weight:700;font-size:28px;letter-spacing:.3px}
  .coach__bio{position:absolute;left:25px;width:290px;top:272px;text-align:center;color:var(--ink);font-size:13.5px;line-height:1.15}
  .map{position:absolute;left:40px;top:388px;width:262px;height:204px;background:linear-gradient(135deg,#eef0ec,#dfe6dc);border:3px solid var(--white)}
  .coach__brand{position:absolute;left:0;width:340px;top:606px;text-align:center;color:var(--white);font-weight:700;font-size:23px}
  .coach__phone{position:absolute;left:0;width:340px;top:636px;display:flex;justify-content:center;align-items:center;gap:8px;color:var(--white);font-family:"Open Sans",sans-serif;font-size:35px;line-height:1}
  .coach__phone svg{width:26px;height:26px}
  .coach__free{position:absolute;left:0;width:340px;top:679px;text-align:center;color:var(--cyan);font-family:"Open Sans",sans-serif;font-weight:600;font-size:29px;line-height:1}
  .coach__consult{position:absolute;left:0;width:340px;top:714px;text-align:center;color:var(--white);font-family:"Open Sans",sans-serif;font-size:24px;line-height:1}
  .hero{position:absolute;left:0;top:0;width:380px;height:520px}
  .cover__brand{position:absolute;left:290px;top:400px;transform-origin:0 0;transform:rotate(-90deg);color:var(--white);font-weight:700;font-size:32px;white-space:nowrap}
  .cover__block{position:absolute;left:0;width:380px;top:598px;text-align:center}
  .cover__name{color:var(--blue-deep);font-weight:700;font-size:22px;line-height:1}
  .cover__sub{color:var(--ink);font-size:16px;line-height:1.2;margin-top:3px}
  .cover__tag1{color:var(--blue-deep);font-weight:700;font-size:25px;line-height:1;margin-top:10px}
  .cover__tag2{color:var(--blue-deep);font-weight:700;font-size:19.5px;line-height:1;margin-top:3px}
  .cover__list{color:var(--ink);font-size:13px;line-height:1.4;margin-top:8px}
</style>
</head>
<body>
<div class="brochure">
  <svg class="brochure__art" viewBox="0 0 1100 802" width="1100" height="802" aria-hidden="true">
    <defs>
      <linearGradient id="introTop" x1="0" y1="0" x2="1" y2="1">
        <stop offset="0" stop-color="#3d85d2"/><stop offset="1" stop-color="#4aa2e8"/>
      </linearGradient>
      <linearGradient id="cyanFade" x1="0" y1="0" x2="0" y2="1">
        <stop offset="0" stop-color="#1ec6f3"/><stop offset="1" stop-color="#6adefb"/>
      </linearGradient>
      <linearGradient id="coachTop" x1="0" y1="0" x2="1" y2="1">
        <stop offset="0" stop-color="#1fc3f2"/><stop offset="1" stop-color="#4ed4f8"/>
      </linearGradient>
    </defs>
    <!-- intro panel -->
    <rect x="0" y="0" width="380" height="802" fill="url(#introTop)"/>
    <path d="M0 500 Q190 420 380 440 L380 802 L0 802 Z" fill="url(#cyanFade)"/>
    <path d="M0 505 Q190 430 380 445 L380 478 Q190 468 0 550 Z" fill="#3b88d6"/>
    <path d="M0 478 Q190 405 380 418" fill="none" stroke="#1ec6f3" stroke-width="6"/>
    <!-- coach panel -->
    <rect x="380" y="0" width="340" height="802" fill="url(#coachTop)"/>
    <path d="M380 440 Q550 420 720 426 L720 802 L380 802 Z" fill="#3b88d6"/>
    <path d="M380 418 Q550 410 720 416" fill="none" stroke="#1ec6f3" stroke-width="6"/>
    <!-- cover panel -->
    <rect x="720" y="0" width="380" height="802" fill="url(#cyanFade)"/>
    <path d="M720 0 L1100 0 L1100 400 Q960 520 720 520 Z" fill="#dfe3e8"/>
    <path d="M720 520 Q960 520 1100 400 L1100 440 Q960 560 720 545 Z" fill="#3b88d6"/>
    <path d="M720 522 Q960 522 1100 402" fill="none" stroke="#ffffff" stroke-width="5"/>
  </svg>

  <section class="panel panel--intro">
    <p class="intro__kicker">HEALTH COACHING FOR</p>
    <h1 class="intro__title">HEALTHCARE PRACTIONERS</h1>
    <p class="intro__lead">Are you overwhelmed and exhausted and feel like there’s no time left for YOU?</p>
    <ul class="intro__list">
      <li>Do you put everyone and everything else before your own health?</li>
      <li>Are you struggling with how to fit in exercise after working 12-15 hour shifts?</li>
      <li>Do you know exactly what you should do to take care of yourself, but it’s just not happening?</li>
      <li>Have you gained weight due to stress-eating, and ready to take it off?</li>
      <li>Are you ready to feel energetic and sexy and to fully love yourself again?</li>
    </ul>
    <div class="photo photo--doctor" role="img" aria-label="Photo of a smiling young doctor in a white coat with a stethoscope"></div>
    <p class="intro__note">As healthcare practitioners, it’s easy to lose sight of your own wants and needs, when you’re so busy taking care of everyone else.</p>
    <p class="intro__call">It’s time to take care of YOU. You deserve it!</p>
    <p class="intro__contact">Are you ready for a change? Let’s talk! Schedule your complimentary 15-minute consultation to discuss your unique situation and your goals. Visit <strong>brightoakwellness.com</strong>, email <strong>lena@brightoakwellness.com</strong> or call Lena at <strong>718.555.0142</strong>.</p>
  </section>

  <section class="panel panel--coach">
    <div class="photo photo--coach" role="img" aria-label="Portrait photo of the health coach"></div>
    <h2 class="coach__name">LENA MARSH</h2>
    <p class="coach__bio">Lena Marsh is a personal trainer, fitness nutritionist, and holistic health coach based in Los Angeles, California. Lena helps clients improve their health, develop sustainable habits, and achieve their goals to be their best, most vibrant selves.</p>
    <div class="map" role="img" aria-label="Street map of the service area"></div>
    <p class="coach__brand">Bright Oak Wellness</p>
    <p class="coach__phone">
      <svg viewBox="0 0 24 24" aria-hidden="true"><rect x="1" y="1" width="22" height="22" rx="4" fill="#fff"/><path d="M8 5.5c.6 0 1.8 2.4 1.8 3 0 .8-1.3 1.2-1.3 1.9 0 1.3 2.8 4.1 4.1 4.1.7 0 1.1-1.3 1.9-1.3.6 0 3 1.2 3 1.8 0 1.3-1.4 2.8-2.8 2.8C10.6 17.8 6.2 13.4 6.2 9.3 6.2 7.9 6.7 5.5 8 5.5z" fill="#3b88d6"/></svg>
      718.555.0142
    </p>
    <p class="coach__free">call for a free</p>
    <p class="coach__consult">15 minute consultation</p>
  </section>

  <section class="panel panel--cover">
    <div class="hero" role="img" aria-label="Photo of a smiling doctor with a stethoscope holding a bowl of fresh salad"></div>
    <p class="cover__brand">Bright Oak Wellness</p>
    <div class="cover__block">
      <p class="cover__name">BRIGHT OAK WELLNESS</p>
      <p class="cover__sub">1-on-1 personal training, los angeles, CA</p>
      <p class="cover__tag1">OPEN UP TO</p>
      <p class="cover__tag2">CHANGE THE WAY YOU LIVE</p>
      <p class="cover__list">GET IN SHAPE | LOSE WEIGHT<br>TONE UP | LOOK &amp; FEEL BETTER THAN EVER</p>
    </div>
  </section>
</div>
</body>
</html>
```